3 Sympathy Cards for Veterinary Hospital

Hi. Brookvale Pet Hospital is a Veterinary Hospital in Australia. We need sympathy cards to send to grieving clients after the loss of their beloved pets.
I have attached the old designs, but we have rebranded and need something to suit our new image.

The cards should have a nice message and appeal to every owner.
They need to match our current branding, but the cards are for the clients, not to advertise us, so not too much branding.
The current cards are attached and they are good because they show a variety of animals so clients might identify with one of them.
I have attached a brown to green gradient that we use on some designs, you don't have to use it, but consider it.
I have attached a logo on background used in some of our new designs, consider using it.
I have attached a font that we use for most new branding.

Target Market(s)

Women 25 to 44

Industry/Entity Type

Veterinary

Font styles to use
Sans Serif
Script

Colors
fac994
cadf82

Requirements
Must have
• IMPORTANT - 3 different designs for the different types of pets.
• 1. Dog.
• 2. Cat.
• 3. Everything else (Rabbits, lizards, ferrets, chickens, birds, mice, rats, snakes)
Nice to have
• Caring and compassionate message.
Should not have
• Too much branding.

```html
<!DOCTYPE html>
<html lang="en">
<head>
<meta charset="utf-8">
<title>Brookvale Pet Hospital – Sympathy Card (Dog)</title>
<link href="https://fonts.googleapis.com/css2?family=Arimo:wght@400;700&family=Lobster+Two:ital,wght@1,700&display=swap" rel="stylesheet">
<style>
  :root {
    --paper: #ffffff;
    --frame: #8a8a8a;
    --peach: #f8c993;
    --leaf: #cadf82;
    --brown: #a2602a;
    --brown-dark: #9a5523;
    --paw-1: #d9b493;
    --paw-2: #c8956b;
    --paw-3: #b67a48;
    --paw-4: #a65e28;
    --fur-light: #e6ad6a;
    --fur-dark: #b9702f;
  }
  * { box-sizing: border-box; }
  html, body {
    margin: 0;
    padding: 0;
    width: 1105px;
    height: 1200px;
    overflow: hidden;
    background: var(--paper);
  }
  .card {
    position: relative;
    width: 1105px;
    height: 1200px;
    border: 1px solid var(--frame);
    background: var(--paper);
    overflow: hidden;
  }
  .card__back {
    position: absolute;
    left: 0; top: 0;
    width: 100%;
    height: 568px;
    border-bottom: 1px solid var(--frame);
  }
  .brand-mark {
    position: absolute;
    left: 452px;
    top: 62px;
    width: 236px;
    text-align: center;
    transform: rotate(180deg);
    font-family: "Arimo", Arial, sans-serif;
    font-weight: 700;
    font-size: 17px;
    letter-spacing: 0.5px;
    color: var(--brown-dark);
    line-height: 1.2;
  }
  .card__front {
    position: absolute;
    left: 0; top: 568px;
    width: 100%;
    height: 632px;
  }
  .swoosh {
    position: absolute;
    left: 0; top: 0;
    width: 1105px;
    height: 632px;
  }
  .hero-photo {
    position: absolute;
    left: 282px;
    top: 142px;
    width: 590px;
    height: 306px;
    border-radius: 46% 46% 12% 12% / 60% 60% 14% 14%;
    background: radial-gradient(ellipse at 60% 40%, var(--fur-light), var(--fur-dark));
  }
  .paw {
    position: absolute;
    border-radius: 42%;
  }
  .paw--1 { left: 1028px; top: 48px;  width: 52px; height: 50px; background: var(--paw-1); }
  .paw--2 { left: 1016px; top: 146px; width: 64px; height: 62px; background: var(--paw-2); }
  .paw--3 { left: 996px;  top: 262px; width: 68px; height: 66px; background: var(--paw-3); }
  .paw--4 { left: 950px;  top: 366px; width: 78px; height: 76px; background: var(--paw-4); }
  .tagline {
    position: absolute;
    left: 406px;
    top: 474px;
    margin: 0;
    font-family: "Arimo", Arial, sans-serif;
    font-weight: 400;
    font-size: 34px;
    letter-spacing: -0.3px;
    color: var(--brown);
    white-space: nowrap;
  }
  .sympathy {
    position: absolute;
    left: 546px;
    top: 538px;
    margin: 0;
    font-family: "Lobster Two", "Brush Script MT", cursive;
    font-style: italic;
    font-weight: 700;
    font-size: 50px;
    color: var(--brown);
    white-space: nowrap;
  }
</style>
</head>
<body>
  <main class="card">
    <section class="card__back">
      <div class="brand-mark">BROOKVALE PET HOSPITAL</div>
    </section>

    <section class="card__front">
      <svg class="swoosh" viewBox="0 0 1105 632" aria-hidden="true">
        <path d="M0,3 Q170,496 646,632 L596,632 Q128,540 0,235 Z" fill="var(--peach)"/>
        <path d="M0,332 Q128,564 553,632 L0,632 Z" fill="var(--leaf)"/>
      </svg>

      <div class="hero-photo" role="img" aria-label="Photograph of a golden puppy lying down, looking towards the viewer"></div>

      <div class="paw paw--1" role="img" aria-label="Paw print"></div>
      <div class="paw paw--2" role="img" aria-label="Paw print"></div>
      <div class="paw paw--3" role="img" aria-label="Paw print"></div>
      <div class="paw paw--4" role="img" aria-label="Paw print"></div>

      <p class="tagline">Forever Loyal, Forever Loved.</p>
      <p class="sympathy">Deepest Sympathy....</p>
    </section>
  </main>
</body>
</html>
```